Brochure design for 3D ultrasound company

I am looking for a clean and modern and edgy brochure for my ultrasound company. We are a fairly new company specialize in 3D/4D ultrasounds.Our brochures will be placed in OB-GYN offices in high end areas around Los Angeles, so we need something that will stand out and capture a modern woman's attention. Our logo is currently in the process of being designed, so I don't have a picture to provide quite yet, however it will be our company name"Kite + Fern" written in a special font that looks like neon lights. I will attach a few images of what our logo will be like, and some initial content that can help provide the layout we would like for the brochure. please feel free to also take a look at our website. www.kitefernscans.example.

Target Market(s)

Upscale trendy women.

Colors
eea4c8
33a6d7
fee18a

Requirements
Should not have
• too many colors.

```html
<!DOCTYPE html>
<html lang="en">
<head>
<meta charset="utf-8">
<title>Kite + Fern Brochure</title>
<link href="https://fonts.googleapis.com/css2?family=Raleway:ital,wght@0,300;0,400;0,500;0,600;0,700;1,700&display=swap" rel="stylesheet">
<style>
:root{
  --stage:#1c1c1c;
  --paper:#ecebef;
  --ink:#2b2b2e;
  --teal:#45bccb;
  --teal-soft:#a9dde4;
  --pink:#e59fc2;
  --rose:#c9557f;
  --rose-soft:#e8b4c7;
  --white:#ffffff;
  --black:#0b0b0b;
}
*{margin:0;padding:0;box-sizing:border-box}
html,body{width:768px;height:1200px;overflow:hidden;background:var(--stage)}
body{font-family:"Raleway",sans-serif;color:var(--ink);position:relative}
.panel{position:absolute;left:43px;width:683px;height:527px;background:var(--paper);overflow:hidden}
.panel--outside{top:47px}
.panel--inside{top:626px}
.abs{position:absolute}
.decor{position:absolute;inset:0}

/* outside */
.whats-what{left:9px;top:78px;width:220px}
.whats-what h2{font-weight:400;font-size:16px;color:var(--teal);letter-spacing:.2px;margin-bottom:14px}
.whats-what p{font-size:8.6px;line-height:1.5;margin-bottom:10px;font-weight:400}
.photo-frame{background:var(--white);padding:7px;box-shadow:0 2px 6px rgba(0,0,0,.25)}
.photo{width:100%;height:100%}
.belly-photo{left:12px;top:337px;width:195px;height:148px}

.contact-card{left:241px;top:78px;width:195px;height:374px;border:1px solid var(--ink);text-align:center;padding-top:12px}
.contact-card .mission{font-size:8.4px;line-height:1.55;padding:0 22px}
.contact-card .brand-name{font-weight:400;font-size:29px;letter-spacing:.5px;margin:22px 0 14px}
.contact-card dl{font-size:9px;line-height:1.25}
.contact-card dt{font-weight:700}
.contact-card dd{margin-bottom:9px}
.contact-card .web{margin-bottom:10px}

.logo-block{left:521px;top:1px;width:96px;height:68px;background:var(--black);display:flex;align-items:center;justify-content:center;color:var(--white);font-size:12px;font-weight:400;letter-spacing:.5px}
.title-box{left:473px;top:79px;width:191px;height:50px;border:1.5px solid var(--ink);display:flex;align-items:center;justify-content:center;font-size:26px;font-weight:500;letter-spacing:.3px;background:rgba(255,255,255,.25)}
.tagline{left:460px;top:134px;width:218px;text-align:center;font-size:10.5px;line-height:1.4;letter-spacing:.3px}
.hero-photo{left:437px;top:165px;width:246px;height:362px}
.call-box{left:473px;top:459px;width:190px;height:52px;background:var(--teal);opacity:.93;color:var(--white);text-align:center}
.call-box .lead{font-size:11px;padding-top:4px}
.call-box .number{font-size:27px;font-weight:300;letter-spacing:.2px;line-height:1.1}

/* inside */
.band{top:0;height:527px}
.band--teal-left{left:8px;width:38px;background:var(--teal)}
.band--pink{left:226px;width:16px;background:var(--pink)}
.band--teal-right{left:242px;width:38px;background:var(--teal)}
.band-label{position:absolute;left:50%;bottom:12px;transform-origin:left bottom;transform:translateX(13px) rotate(-90deg);white-space:nowrap;color:var(--white);font-size:25px;font-weight:400;letter-spacing:.3px}
.band--teal-right .band-label{bottom:14px}
.feature-photo{left:46px;top:0;width:180px;height:259px}
.feature{left:55px;top:264px;width:165px}
.pkg-head{display:flex;justify-content:space-between;font-weight:700;color:var(--teal);font-size:11px}
.feature .pkg-head{justify-content:flex-start;gap:16px}
.pkg-list{list-style:none;font-size:9.5px;line-height:1.28;margin-top:11px}
.pkg-list li{padding-left:8px;position:relative}
.pkg-list li::before{content:"·";position:absolute;left:0}
.rule{height:1px;background:var(--ink);width:54px}
.feature-cta{left:55px;top:393px;width:165px;text-align:center}
.feature-cta .rule{margin:0 auto}
.feature-cta .prompt{font-style:italic;font-weight:700;color:var(--rose-soft);font-size:12px;line-height:1.3;margin:10px 0 12px}
.feature-cta .small{font-size:7.6px;line-height:1.35;margin-bottom:8px}
.feature-cta .rule:last-child{margin-top:6px}

.banner-photo{left:290px;top:0;width:393px;height:90px}
.banner-strip{left:290px;top:90px;width:393px;height:28px;background:var(--teal-soft)}
.intro{left:290px;top:126px;width:380px;font-size:9.6px;line-height:1.25;padding-left:10px}
.pkg-photo{left:289px;width:110px;height:100px;padding:6px}
.pkg{left:409px;width:246px}
.pkg .pkg-head{border:1px solid var(--teal);background:var(--white);height:25px;align-items:center;padding:0 6px;font-size:11px}
.pkg .pkg-list{margin-top:12px;padding-left:6px}
</style>
</head>
<body>

<section class="panel panel--outside">
  <svg class="decor" viewBox="0 0 683 527" aria-hidden="true">
    <polygon points="500,0 683,0 683,160 610,0" fill="#e7a9c0" opacity=".55"/>
    <polygon points="470,60 560,60 683,200 683,250" fill="#e2aec2" opacity=".4"/>
    <polygon points="0,380 80,527 0,527" fill="#d6839f" opacity=".6"/>
    <polygon points="60,420 240,420 190,527 120,527" fill="#e7a9c0" opacity=".45"/>
    <polygon points="0,470 60,527 0,527" fill="#c9557f" opacity=".5"/>
  </svg>

  <div class="abs whats-what">
    <h2>WHAT’S WHAT...</h2>
    <p>2D is the traditional black and white photo—you know, the one that you want to get emotional about, but you don’t know what you’re looking at.</p>
    <p>3D is an image of the fetus and it’s features. So you can see the baby has dad’s nose, and mom’s lips.</p>
    <p>4D is 3D, but with motion. You can see the baby yawn, move it’s arm, or even give you a smile.</p>
    <p>HD is also 3D, but better. Now you can see a rendering of the baby’s skin making it the most realistic fetal image possible..we are one of the few in Los Angeles that have the newest HD capable machines</p>
  </div>
  <div class="abs photo-frame belly-photo">
    <div class="photo" role="img" aria-label="Photo of a pregnant belly with hands holding an ultrasound print" style="background:linear-gradient(160deg,#e9e3e0,#d8b9ab 55%,#3a3536)"></div>
  </div>

  <div class="abs contact-card">
    <p class="mission">Kite + Fern is a mobile 3D ultrasound company servicing Los Angeles, and surrounding areas. We take great pride in being one of LA’s first mobile Ultrasound companies and for being an all female business! Our mission is to provide an unforgettable experience for expectant mothers in the comfort of their home!</p>
    <p class="brand-name">KITE + FERN</p>
    <dl>
      <dt>Telephone:</dt><dd>(310) 555-0142</dd>
      <dd class="web">www.kitefernscans.example</dd>
      <dt>Email:</dt><dd>info@kitefernscans.example</dd>
      <dt>Instagram:</dt><dd>kite_fern</dd>
      <dt>Facebook:</dt><dd>@kitefernscans</dd>
    </dl>
  </div>

  <div class="abs hero-photo" role="img" aria-label="Photo of a pregnant woman in a white crop top and jeans" style="background:linear-gradient(180deg,rgba(236,235,239,0),rgba(226,205,196,.7) 40%,rgba(214,180,168,.8) 70%,#5c7898)"></div>
  <div class="abs logo-block">Kite + Fern</div>
  <div class="abs title-box">KITE + FERN</div>
  <p class="abs tagline">ULTRASOUND<br>IN THE COMFORT OF YOUR HOME</p>
  <div class="abs call-box">
    <p class="lead">Call today!</p>
    <p class="number">310-555-0142</p>
  </div>
</section>

<section class="panel panel--inside">
  <div class="abs band band--teal-left"><span class="band-label">OUR MOST POPULAR PACKAGE</span></div>
  <div class="abs feature-photo" role="img" aria-label="Photo of a pregnant woman kneeling on a bed holding ultrasound prints" style="background:linear-gradient(180deg,#d9d4cf,#ece9e6 45%,#f3f1ef)"></div>
  <div class="abs feature">
    <p class="pkg-head"><span>THE BIG REVEAL!!</span><span>$225.00</span></p>
    <ul class="pkg-list">
      <li>25 minute 3D/4D/HD live session</li>
      <li>5 black and white pictures</li>
      <li>5 color pictures</li>
      <li>Email or USB flash drive with all images</li>
      <li>Record and hear heartbeat</li>
      <li>Confirm gender</li>
    </ul>
  </div>
  <div class="abs feature-cta">
    <div class="rule"></div>
    <p class="prompt">Ready for your baby’s<br>first photoshoot?</p>
    <p class="small">Give us a call to schedule<br>an appointment (310) 555-0142</p>
    <p class="small">or visit our website<br>www.kitefernscans.example</p>
    <div class="rule"></div>
  </div>

  <div class="abs band band--pink"></div>
  <div class="abs band band--teal-right"><span class="band-label">SERVICES + PRICING</span></div>

  <div class="abs banner-photo" role="img" aria-label="Photo of a row of toy baby dolls on a pink background" style="background:linear-gradient(180deg,#f2c3c4,#f0b6b8)"></div>
  <div class="abs banner-strip"></div>
  <p class="abs intro">We are available for private in-home screenings, gender reveals, baby showers, or any other special occasion!</p>

  <div class="abs photo-frame pkg-photo" style="top:170px"><div class="photo" role="img" aria-label="Photo of expecting parents holding gender reveal cards" style="background:linear-gradient(135deg,#c98a6a,#e8e2de 50%,#4d6a86)"></div></div>
  <div class="abs pkg" style="top:173px">
    <p class="pkg-head"><span>PEEK-A-BOO</span><span>$125.00</span></p>
    <ul class="pkg-list"><li>15 minute 2D session</li><li>3 black and white images</li><li>Listen to baby’s heartbeat</li><li>Confirm gender</li></ul>
  </div>

  <div class="abs photo-frame pkg-photo" style="top:284px"><div class="photo" role="img" aria-label="Photo of two pregnant women in crop tops" style="background:linear-gradient(135deg,#ea9fb3,#e7cdbf 50%,#8fb0cc)"></div></div>
  <div class="abs pkg" style="top:287px">
    <p class="pkg-head"><span>HELLO, MOMMA</span><span>$165.00</span></p>
    <ul class="pkg-list"><li>15 minute 3D/4D /HD live session</li><li>3 black and white images</li><li>2 color images</li><li>Listen to baby’s heartbeat</li><li>Confirm gender</li></ul>
  </div>

  <div class="abs photo-frame pkg-photo" style="top:400px"><div class="photo" role="img" aria-label="Photo of a sleeping newborn on a soft blanket" style="background:linear-gradient(135deg,#dfe3ea,#ecd3c6 60%,#f0ece9)"></div></div>
  <div class="abs pkg" style="top:403px">
    <p class="pkg-head"><span>V.I.B (VERY IMPORTANT BABY)</span><span>$325.00</span></p>
    <ul class="pkg-list"><li>30 min 3D/4D/HD live session on our projector</li><li>10 color images</li><li>Email or USB with all images</li><li>Record and hear heartbeat</li><li>Confirm gender</li></ul>
  </div>
</section>

</body>
</html>
```